Business software developers new website

We need to redesign our website. Our current website is http://www.plumvista.net/index.html, which is outdated and needs a new look. We moved out from web design and have concentrated more on the back end of the systems, for example, system support and security and cloud-based applications. Our major clients include both private and government sectors. We would like to see some designs that are all in one page, simple and clean. Prefer illustrator or obstructed images instead of real-life photos. Must look futuristic yet friendly. Attached the new logo for your references and good luck.

Target Market(s)

Medium to big company for their IT or data management. Either improve or upgrade their current system.

Industry/Entity Type

Business Software

Number of Pages Required

1 page

Colors

Designer to choose colors to be used in the design.

Requirements
Must have
• Simple and clean. Individual assets must be provided in the correct size and format(png or jpeg). Prefer Goggle fonts. Even though the logo color is red, grey and black, still prefer some modern colors that go well with red. When design, must consider the possibility to convert it into responsive.
Nice to have
• White background
Should not have
• real life photos, no slider

```html
<!DOCTYPE html>
<html lang="en">
<head>
<meta charset="utf-8">
<title>Plumvista — Business Software</title>
<link href="https://fonts.googleapis.com/css2?family=Montserrat:wght@300;400;500;600;700&display=swap" rel="stylesheet">
<style>
:root{
  --red:#e8344b;
  --red-deep:#d6263d;
  --red-soft:#f25a6a;
  --dark:#2a2a2e;
  --darker:#222226;
  --grey-bg:#f2f2f4;
  --text:#3c3c44;
  --muted:#8a8a94;
  --line:#e3e3e8;
  --white:#ffffff;
}
*{box-sizing:border-box;margin:0;padding:0}
html,body{width:1200px;height:3100px;overflow:hidden}
body{font-family:"Montserrat",Arial,sans-serif;color:var(--text);background:var(--white);position:relative}
section,header,footer{position:relative;width:1200px}

/* Header / hero */
.hero{height:420px;background:linear-gradient(100deg,var(--red-soft) 0%,var(--red) 55%,var(--red-deep) 100%);color:var(--white);overflow:hidden}
.nav{position:absolute;top:16px;left:120px;right:120px;height:26px;display:flex;align-items:center}
.brand{display:flex;align-items:center;gap:6px;font-weight:600;font-size:17px;color:var(--white)}
.brand-dot{width:9px;height:9px;border-radius:50%;background:var(--white)}
.menu{display:flex;gap:18px;margin-left:auto;font-size:9px;font-weight:500}
.menu a{color:var(--white);text-decoration:none;opacity:.85}
.menu a.active{opacity:1;border-bottom:1px solid var(--white);padding-bottom:2px}
.call{margin-left:26px;display:flex;align-items:center;gap:6px;border:1px solid rgba(255,255,255,.7);border-radius:12px;padding:4px 10px;font-size:8px;font-weight:600}
.social{display:flex;gap:6px;margin-left:18px}
.social span{width:9px;height:9px;border-radius:50%;background:rgba(255,255,255,.85)}
.hero-copy{position:absolute;left:230px;top:120px;width:380px}
.hero-copy h1{font-size:25px;font-weight:500;line-height:1.32}
.hero-copy p{font-size:9px;line-height:1.6;margin-top:12px;opacity:.85;width:230px}
.btn-outline{display:inline-block;margin-top:22px;border:1px solid var(--white);border-radius:14px;padding:7px 18px;font-size:8px;font-weight:600;letter-spacing:.5px;color:var(--white)}
.hero-art{position:absolute;left:640px;top:40px;width:360px;height:360px;border-radius:30px;background:radial-gradient(circle at 55% 50%,rgba(255,255,255,.55),rgba(120,150,230,.35) 45%,rgba(255,255,255,0) 72%)}

/* Intro */
.intro{height:720px;background:var(--dark);color:var(--white);text-align:center;overflow:hidden}
.pill{display:inline-block;margin-top:58px;background:var(--red);border-radius:10px;padding:5px 14px;font-size:8px;font-weight:700;letter-spacing:.8px}
.intro h2{font-size:19px;font-weight:400;line-height:1.45;width:560px;margin:14px auto 0}
.intro .small{font-size:9px;line-height:1.7;width:600px;margin:22px auto 0;opacity:.75}
.intro .enquire{margin-top:26px;font-size:9px;font-weight:700;letter-spacing:.6px}
.intro .enquire::after{content:"";display:block;width:70px;height:1px;background:var(--red);margin:8px auto 0}
.dots{position:absolute;inset:0;pointer-events:none}
.mountains{position:absolute;left:0;bottom:0}
.services{position:absolute;left:230px;top:380px;width:740px;height:265px;background:var(--white);box-shadow:0 10px 30px rgba(0,0,0,.12);display:flex;color:var(--text)}
.service{flex:1;padding:30px 34px;text-align:center;border-right:1px solid var(--line)}
.service:last-child{border-right:none}
.service svg{display:block;margin:0 auto}
.service h3{font-size:12px;font-weight:500;margin-top:14px}
.service p{font-size:8px;line-height:1.7;color:var(--muted);margin-top:8px}
.btn-more{position:absolute;left:50%;bottom:-1px;transform:translate(-50%,50%);background:var(--white);border:1px solid var(--line);border-radius:12px;padding:6px 16px;font-size:7px;font-weight:700;letter-spacing:.6px}

/* Why choose us */
.why{height:420px}
.why-art{position:absolute;left:225px;top:60px;width:340px;height:310px;background:radial-gradient(circle,#ebe9fb 0%,#f4f3fb 45%,rgba(255,255,255,0) 70%);clip-path:polygon(25% 3%,75% 3%,100% 50%,75% 97%,25% 97%,0 50%)}
.why-copy{position:absolute;left:665px;top:95px;width:320px}
.why-copy h2{font-size:25px;font-weight:400}
.why-list{list-style:none;margin-top:18px}
.why-list li{display:flex;gap:10px;align-items:flex-start;font-size:8.5px;line-height:1.6;color:var(--muted);margin-bottom:12px}
.why-list li svg{flex:none;margin-top:1px}
.btn-red{display:inline-block;margin-top:8px;background:var(--red);color:var(--white);border-radius:14px;padding:7px 18px;font-size:8px;font-weight:700;letter-spacing:.5px}

/* Testimonials */
.clients{height:500px;background:var(--grey-bg);text-align:center;padding-top:70px}
.section-title{font-size:22px;font-weight:400;color:var(--text)}
.section-sub{font-size:8.5px;line-height:1.7;color:var(--muted);width:420px;margin:10px auto 0}
.cards{display:flex;gap:24px;justify-content:center;margin-top:38px}
.quote-card{width:235px;height:220px;background:var(--white);box-shadow:0 6px 20px rgba(0,0,0,.06);text-align:left;padding:22px 20px}
.quote-mark{font-size:38px;line-height:.8;color:var(--red);font-weight:700;font-family:Georgia,serif}
.quote-card p{font-size:8px;line-height:1.75;color:var(--muted);margin-top:8px}
.quote-card .who{margin-top:14px;font-size:9px;font-weight:600;color:var(--red)}
.quote-card .role{font-size:7.5px;color:var(--muted);margin-top:2px}

/* Blog */
.blog{height:520px;text-align:center;padding-top:72px}
.post{width:235px;background:var(--white);box-shadow:0 6px 20px rgba(0,0,0,.07);text-align:left}
.post-img{height:120px}
.post-body{padding:14px 14px 16px}
.post h3{font-size:11px;font-weight:500;color:var(--text)}
.post .date{font-size:7px;color:var(--red);margin-top:4px}
.post p{font-size:8px;line-height:1.7;color:var(--muted);margin-top:8px}
.post .more{display:inline-block;margin-top:10px;font-size:7.5px;font-weight:600;color:var(--text);border-bottom:1px solid var(--red)}

/* Newsletter */
.newsletter{height:240px;background:linear-gradient(100deg,var(--red-soft),var(--red) 55%,var(--red-deep));color:var(--white);text-align:center;padding-top:78px}
.newsletter h2{font-size:20px;font-weight:400}
.newsletter p{font-size:8.5px;line-height:1.7;width:440px;margin:10px auto 0;opacity:.85}
.subscribe{width:290px;height:26px;margin:20px auto 0;background:var(--white);border-radius:13px;display:flex;align-items:center;justify-content:space-between;padding:0 12px;font-size:8px;color:var(--muted)}

/* Footer */
.footer{height:300px;background:var(--darker);color:var(--white)}
.foot-cols{position:absolute;left:230px;top:70px;width:740px;display:flex}
.foot-col{flex:1}
.foot-col h4{font-size:10px;font-weight:600}
.foot-col ul{list-style:none;margin-top:12px}
.foot-col li{font-size:8px;color:#a4a4ad;margin-bottom:7px}
.foot-bottom{position:absolute;left:0;right:0;top:250px;text-align:center;font-size:7.5px;color:#8c8c95}
.foot-social{display:flex;gap:7px;justify-content:center;margin-bottom:8px}
.foot-social span{width:9px;height:9px;border-radius:50%;background:#8c8c95}
</style>
</head>
<body>

<header class="hero">
  <nav class="nav">
    <div class="brand"><span class="brand-dot"></span>plumvista</div>
    <div class="menu">
      <a class="active" href="#">Home</a><a href="#">About</a><a href="#">Services</a><a href="#">Blog</a><a href="#">Contact</a>
    </div>
    <div class="call">
      <svg width="8" height="8" viewBox="0 0 24 24"><path fill="#fff" d="M6.6 10.8a15 15 0 0 0 6.6 6.6l2.2-2.2c.3-.3.7-.4 1-.2 1.1.4 2.3.6 3.6.6.6 0 1 .4 1 1V20c0 .6-.4 1-1 1A17 17 0 0 1 3 4c0-.6.4-1 1-1h3.5c.6 0 1 .4 1 1 0 1.3.2 2.5.6 3.6.1.3 0 .7-.2 1z"/></svg>
      (02) 5550 1234
    </div>
    <div class="social"><span></span><span></span><span></span><span></span></div>
  </nav>
  <div class="hero-copy">
    <h1>We promised to bring the best solutions to your business</h1>
    <p>Back end systems, support and security built for growing teams.</p>
    <span class="btn-outline">GET IN TOUCH</span>
  </div>
  <div class="hero-art" role="img" aria-label="Isometric illustration of server racks, a laptop and cloud symbols with a technician"></div>
</header>

<section class="intro">
  <svg class="dots" width="1200" height="720" aria-hidden="true">
    <g fill="#ffffff" opacity=".25">
      <circle cx="160" cy="90" r="2"/><circle cx="300" cy="200" r="1.5"/><circle cx="980" cy="120" r="2"/><circle cx="1060" cy="260" r="1.5"/><circle cx="210" cy="330" r="1.5"/><circle cx="880" cy="330" r="2"/><circle cx="420" cy="60" r="1.5"/><circle cx="760" cy="50" r="1.5"/>
    </g>
    <g fill="none" stroke="#ffffff" opacity=".08">
      <polygon points="120,260 160,237 200,260 200,306 160,329 120,306"/>
      <polygon points="1000,180 1040,157 1080,180 1080,226 1040,249 1000,226"/>
    </g>
  </svg>
  <svg class="mountains" width="1200" height="360" viewBox="0 0 1200 360" aria-hidden="true">
    <polygon fill="#ffffff" points="0,360 0,250 180,150 330,230 520,110 700,220 880,120 1040,210 1200,140 1200,360"/>
  </svg>
  <span class="pill">WELCOME TO PLUMVISTA</span>
  <h2>Lorem ipsum dolor sit amet, consectetur adipiscing elit cras sodales non purus non consequat. Suspendisse accumsan velit vel congue lobortis.</h2>
  <p class="small">Praesent sed tortor facilisis, tincidunt massa in lacus ut ligula vehicula. Curabitur nisi libero, pretium id metus vel, consequat tempor erat. Mauris eu sapien, facilisis quis lorem.</p>
  <div class="enquire">ENQUIRE US FOR A FREE DEMO</div>

  <div class="services">
    <div class="service">
      <svg width="46" height="46" viewBox="0 0 46 46" aria-hidden="true"><circle cx="23" cy="23" r="22" fill="#fdecee"/><rect x="12" y="13" width="22" height="15" rx="1.5" fill="none" stroke="#e8344b" stroke-width="1.6"/><path d="M19 33h8M23 28v5" stroke="#e8344b" stroke-width="1.6"/></svg>
      <h3>System Support</h3>
      <p>Nullam feugiat nisi varius ut sagittis. Integer lacinia nisl a vulputate faucibus, sed lectus consectetur dolor.</p>
    </div>
    <div class="service">
      <svg width="46" height="46" viewBox="0 0 46 46" aria-hidden="true"><circle cx="23" cy="23" r="22" fill="#e7f6f4"/><path d="M23 11l10 4v7c0 7-4.5 11-10 13-5.5-2-10-6-10-13v-7z" fill="none" stroke="#27a99a" stroke-width="1.6"/><path d="M18.5 23l3.2 3.2 5.8-6" fill="none" stroke="#27a99a" stroke-width="1.6"/></svg>
      <h3>Security</h3>
      <p>Curabitur blandit tempus porttitor, donec sed odio dui. Aenean lacinia bibendum nulla sed consectetur elit.</p>
    </div>
    <div class="service">
      <svg width="46" height="46" viewBox="0 0 46 46" aria-hidden="true"><circle cx="23" cy="23" r="22" fill="#eaf0fb"/><path d="M15 29h17a5 5 0 0 0 0-10 7 7 0 0 0-13.5-1.5A5.8 5.8 0 0 0 15 29z" fill="none" stroke="#4a74c9" stroke-width="1.6"/></svg>
      <h3>Cloud-based Applications</h3>
      <p>Maecenas faucibus mollis interdum. Vivamus sagittis lacus vel augue laoreet rutrum faucibus dolor auctor.</p>
    </div>
    <span class="btn-more">FIND OUT MORE</span>
  </div>
</section>

<section class="why">
  <div class="why-art" role="img" aria-label="Isometric illustration of a shield beside server blocks inside a hexagon"></div>
  <div class="why-copy">
    <h2>Why Choose Us</h2>
    <ul class="why-list">
      <li><svg width="11" height="11" viewBox="0 0 12 12"><circle cx="6" cy="6" r="5.5" fill="none" stroke="#e8344b"/><path d="M3.5 6.2l1.7 1.6 3.3-3.5" fill="none" stroke="#e8344b"/></svg>Lorem ipsum dolor sit amet, quis ligula. Fusce eget metus, dapibus faucibus molestie a erat.</li>
      <li><svg width="11" height="11" viewBox="0 0 12 12"><circle cx="6" cy="6" r="5.5" fill="none" stroke="#e8344b"/><path d="M3.5 6.2l1.7 1.6 3.3-3.5" fill="none" stroke="#e8344b"/></svg>Phasellus laoreet est purus, sodales vitae feugiat nec.</li>
      <li><svg width="11" height="11" viewBox="0 0 12 12"><circle cx="6" cy="6" r="5.5" fill="none" stroke="#e8344b"/><path d="M3.5 6.2l1.7 1.6 3.3-3.5" fill="none" stroke="#e8344b"/></svg>Etiam tincidunt, sapien a posuere iaculis, felis nulla suscipit lectus, ac tempor nunc.</li>
      <li><svg width="11" height="11" viewBox="0 0 12 12"><circle cx="6" cy="6" r="5.5" fill="none" stroke="#e8344b"/><path d="M3.5 6.2l1.7 1.6 3.3-3.5" fill="none" stroke="#e8344b"/></svg>Duis tellus ornare nulla, a porta magna pretium.</li>
    </ul>
    <span class="btn-red">GET IN TOUCH</span>
  </div>
</section>

<section class="clients">
  <h2 class="section-title">What our client speak about us</h2>
  <p class="section-sub">Etiam tincidunt, sapien a posuere iaculis, felis nulla suscipit lectus, ac tempor nunc sem eget ligula. Donec sollicitudin lorem.</p>
  <div class="cards">
    <div class="quote-card">
      <div class="quote-mark">&ldquo;</div>
      <p>Curabitur pulvinar semper nisi vitae feugiat. Integer lacinia nisl a vulputate faucibus. Donec ac metus pretium, iaculis est vel, posuere massa, quis porta felis. Sed vel dictum tellus vitae.</p>
      <div class="who">Lucille Ardmore</div>
      <div class="role">Operations Manager</div>
    </div>
    <div class="quote-card">
      <div class="quote-mark">&ldquo;</div>
      <p>Vestibulum ante ipsum primis in faucibus orci luctus et ultrices posuere cubilia. Nam vitae neque ut mi posuere consequat. Phasellus eu nunc at nisi blandit mollis aliquam.</p>
      <div class="who">Lucille Ardmore</div>
      <div class="role">Operations Manager</div>
    </div>
    <div class="quote-card">
      <div class="quote-mark">&ldquo;</div>
      <p>Morbi dignissim orci non lorem efficitur, a congue nisi ullamcorper. Fusce sagittis lacus at erat aliquam, eget blandit ipsum tempor. Duis elementum magna sed risus.</p>
      <div class="who">Lucille Ardmore</div>
      <div class="role">Operations Manager</div>
    </div>
  </div>
</section>

<section class="blog">
  <h2 class="section-title">Latest from our Blog</h2>
  <p class="section-sub">Etiam tincidunt, sapien a posuere iaculis, felis nulla suscipit lectus, ac tempor nunc sem eget ligula. Donec sollicitudin lorem.</p>
  <div class="cards">
    <article class="post">
      <div class="post-img" role="img" aria-label="Illustration of a laptop on a desk" style="background:linear-gradient(135deg,#3d6fa8,#1f3552)"></div>
      <div class="post-body">
        <h3>Title of the blog</h3>
        <div class="date">Posted 12 March 2024</div>
        <p>Curabitur pulvinar semper nisi vitae feugiat. Integer lacinia nisl a vulputate faucibus, donec ac metus.</p>
        <span class="more">READ MORE</span>
      </div>
    </article>
    <article class="post">
      <div class="post-img" role="img" aria-label="Illustration of hands working together over a table" style="background:linear-gradient(135deg,#b9a58c,#5c4c3d)"></div>
      <div class="post-body">
        <h3>Title of the blog</h3>
        <div class="date">Posted 08 March 2024</div>
        <p>Vestibulum ante ipsum primis in faucibus orci luctus. Nam vitae neque ut mi posuere consequat nunc.</p>
        <span class="more">READ MORE</span>
      </div>
    </article>
    <article class="post">
      <div class="post-img" role="img" aria-label="Illustration of code on a screen" style="background:linear-gradient(135deg,#2c4a78,#121b2c)"></div>
      <div class="post-body">
        <h3>Title of the blog</h3>
        <div class="date">Posted 02 March 2024</div>
        <p>Morbi dignissim orci non lorem efficitur, a congue nisi ullamcorper. Fusce sagittis lacus at erat.</p>
        <span class="more">READ MORE</span>
      </div>
    </article>
  </div>
</section>

<section class="newsletter">
  <h2>Sign up to join our tech insights program</h2>
  <p>Etiam tincidunt, sapien a posuere iaculis, felis nulla suscipit lectus, ac tempor nunc sem eget ligula. Donec sollicitudin lorem at nisl.</p>
  <div class="subscribe">Enter your email address
    <svg width="11" height="11" viewBox="0 0 24 24"><path fill="#e8344b" d="M2 21l21-9L2 3v7l15 2-15 2z"/></svg>
  </div>
</section>

<footer class="footer">
  <div class="foot-cols">
    <div class="foot-col"><h4>Links</h4><ul><li>Home</li><li>About</li><li>Services</li><li>Blog</li></ul></div>
    <div class="foot-col"><h4>Our Services</h4><ul><li>System Support</li><li>Security</li><li>Cloud-based Applications</li></ul></div>
    <div class="foot-col"><h4>Support</h4><ul><li>Contact Us</li><li>FAQ</li><li>Terms &amp; Privacy</li></ul></div>
    <div class="foot-col"><h4>Contact Us</h4><ul><li>42 Harbour Lane</li><li>Riverton NSW 2190</li><li>(02) 5550 1234</li><li>hello@plumvista.net</li></ul></div>
  </div>
  <div class="foot-bottom">
    <div class="foot-social"><span></span><span></span><span></span><span></span></div>
    Copyright © 2024 Plumvista Pty Ltd. All Rights Reserved.
  </div>
</footer>

</body>
</html>
```